Website for a online coaching platform

I would like a website designed with the same content the same as the one below:

https://www.morvel-tane.com/

New practitioner Pieter Vosloorink

Target Market(s)

Injured athletes for treatment and medcal professionals for education

Industry/Entity Type

Professional sport and medical education

Coding

Coded - Design and coding required

Number of Pages Required

5+ page

Colors

Designer to choose colors to be used in the design.

Requirements
Must have
• Same amount and format of pages as sample website

```html
<!DOCTYPE html>
<html lang="en">
<head>
<meta charset="utf-8">
<title>PVK Performance</title>
<link href="https://fonts.googleapis.com/css2?family=Krona+One&family=Inter:ital,wght@0,400;0,600;0,700;1,700&display=swap" rel="stylesheet">
<style>
:root{
  --bg:#0d0d0d;
  --band:#1a1a1a;
  --green:#7cc242;
  --orange:#f4a949;
  --blue:#2f7fd8;
  --white:#ffffff;
  --muted:#d6d6d6;
  --line:#3a3a3a;
}
*{margin:0;padding:0;box-sizing:border-box}
html,body{width:1200px;height:3344px;overflow:hidden;background:var(--bg)}
body{position:relative;font-family:"Inter",Arial,sans-serif;color:var(--white)}
.abs{position:absolute}
.display{font-family:"Krona One",Arial,sans-serif;font-weight:400}
.accent{color:var(--green)}
.btn{position:absolute;display:flex;align-items:center;justify-content:center;background:var(--blue);color:var(--white);font-size:13px;letter-spacing:.3px;text-transform:uppercase}

/* header */
.brand{left:100px;top:20px;font-family:"Krona One",sans-serif;font-size:22px;line-height:26px;color:var(--white)}
.brand small{display:block;font-size:9px;letter-spacing:2.5px;line-height:14px}
.main-nav{right:243px;top:32px;display:flex;gap:18px;font-size:12.5px;text-transform:uppercase;white-space:nowrap}
.nav-book{left:975px;top:22px;width:125px;height:34px}

/* hero */
.hero{left:0;top:0;width:1200px;height:610px;background:linear-gradient(180deg,#16272a 0%,#1d3a38 35%,#142523 70%,#0d0d0d 100%)}
.hero-title{left:0;top:264px;width:1200px;text-align:center;font-size:46px;line-height:54px}
.hero-sub{left:0;top:442px;width:1200px;text-align:center;font-size:15px;font-weight:700}

/* about blocks */
.section-title{font-size:34px;line-height:41px}
.body-copy{width:440px;font-size:12.6px;line-height:21.2px;color:var(--muted)}
.frame-orange{background:var(--orange)}
.frame-green{background:var(--green)}
.photo{background:linear-gradient(135deg,#b8342c 0%,#2a3f8c 45%,#d9a73a 70%,#8c1f2a 100%)}
.photo-speaker{background:linear-gradient(135deg,#1d5a92 0%,#2b6ea8 40%,#3a3a3a 70%,#1b4d6e 100%)}

/* services */
.card-img{top:1265px;width:321px;height:199px}
.card-label{top:1482px;width:321px;text-align:center;font-size:14px}

/* testimonials */
.band{left:0;top:1636px;width:1200px;height:574px;background:var(--band)}
.player-photo{left:100px;top:1712px;width:432px;height:414px;background:linear-gradient(160deg,#3e4a3a 0%,#1f7a3d 45%,#e8e8e8 75%,#4a5a3e 100%)}
.player-frame{left:112px;top:1722px;width:431px;height:413px;border:1px solid var(--orange)}
.quote-mark{left:646px;top:1788px}
.quote{left:648px;top:1853px;width:452px;font-size:15px;line-height:23px;font-style:italic;font-weight:700}
.quote-rule{left:648px;top:2039px;width:451px;height:1px;background:var(--line)}
.avatar{left:647px;top:2070px;width:50px;height:50px;border-radius:50%;border:1px dashed var(--orange);background:#2c4a36}
.who{left:716px;top:2076px;font-size:15px;font-weight:600}
.role{left:716px;top:2101px;font-size:12.5px;color:var(--muted)}
.arrow{width:38px;height:38px;border-radius:50%;background:var(--green);top:1904px}

/* events */
.event{top:2874px;width:214px;height:126px;border-left:2px solid var(--orange);padding-left:6px}
.event-date{font-size:14.5px;font-weight:700;color:var(--orange);line-height:18px}
.event-name{margin-top:6px;font-family:"Krona One",sans-serif;font-size:11px;line-height:21px;letter-spacing:.2px}
.event-place{margin-top:6px;font-size:12px;color:var(--muted)}

/* footer */
.foot-brand{left:100px;top:3170px;font-family:"Krona One",sans-serif;font-size:34px;line-height:40px}
.foot-brand small{display:block;font-size:12px;letter-spacing:3.5px;line-height:22px}
.foot-nav{top:3197px;font-size:13px;font-weight:700;text-transform:uppercase}
.social{top:3184px;width:40px;height:40px;border-radius:50%;background:var(--blue)}
.foot-rule{left:100px;top:3286px;width:1000px;height:1px;background:#5a5a5a}
.copyright{left:0;top:3311px;width:1200px;text-align:center;font-size:11px;color:var(--muted)}
</style>
</head>
<body>

<div class="abs hero" role="img" aria-label="Photo of two athletes running sprint drills on an indoor training pitch"></div>

<header>
  <div class="abs brand">PVK<small>PERFORMANCE</small></div>
  <nav class="abs main-nav">
    <span>About PVK</span><span>Rehabilitation Specialist</span><span>Events</span><span>Contact</span>
  </nav>
  <a class="btn nav-book">Book PVK</a>
</header>

<h1 class="abs hero-title display">ACL Rehabilitation<br>&amp; Return to Play<br>Decision Making</h1>
<p class="abs hero-sub">Expertise in Rehabilitation, Injury Prevention and Athletic Performance</p>

<!-- about -->
<h2 class="abs section-title display" style="left:100px;top:738px"><span class="accent">About</span> PVK<br>Performance</h2>
<p class="abs body-copy" style="left:100px;top:835px">Cian Moran PhD MSc blends his work as a sports physiotherapist, strength and conditioning coach, researcher and lecturer, supporting individual athletes and elite squads across a wide range of sports and disciplines. He currently leads Elite Performance and Development at Alvera Clinic, Doha, Qatar, and travels widely to work with athletes and professional clubs. He divides his time between Qatar and Ireland with his wife Sinead and their three children Aoife, Conor and Niamh.</p>
<a class="btn" style="left:100px;top:1009px;width:125px;height:33px">Read More</a>
<div class="abs frame-orange" style="left:705px;top:670px;width:394px;height:407px"></div>
<div class="abs frame-green" style="left:578px;top:708px;width:393px;height:410px"></div>
<div class="abs photo" style="left:591px;top:682px;width:497px;height:425px" role="img" aria-label="Graduation ceremony photo of the practitioner receiving his doctorate in academic robes"></div>

<!-- services -->
<h2 class="abs display" style="left:0;top:1192px;width:1200px;text-align:center;font-size:33px"><span class="accent">Rehabilitation</span> Specialist</h2>
<div class="abs card-img" style="left:100px;background:linear-gradient(90deg,#c9ced6 0%,#dfe3ea 45%,#f6f6f8 55%,#f3dde4 100%)" role="img" aria-label="Treadmill running lab with EMG analysis chart"></div>
<div class="abs card-img" style="left:440px;background:linear-gradient(135deg,#2a4b8c 0%,#7a7f86 50%,#3a3d42 100%)" role="img" aria-label="Coach guiding an athlete through a gym rehabilitation exercise"></div>
<div class="abs card-img" style="left:779px;background:linear-gradient(180deg,#000 0%,#0a0a0a 75%,#3a3a3a 100%)" role="img" aria-label="Digital motion capture skeleton models"></div>
<p class="abs card-label display" style="left:100px">Alvera Clinic</p>
<p class="abs card-label display" style="left:440px">Elite Athlete Rehabilitation</p>
<p class="abs card-label display" style="left:779px">Digital Consults</p>
<a class="btn" style="left:538px;top:1529px;width:124px;height:33px">Book PVK</a>

<!-- testimonials -->
<section>
  <div class="abs band"></div>
  <div class="abs player-frame"></div>
  <div class="abs player-photo" role="img" aria-label="Rugby player in a green jersey carrying the ball"></div>
  <h2 class="abs display" style="left:648px;top:1719px;font-size:31px">Testimonials</h2>
  <svg class="abs quote-mark" width="50" height="40" viewBox="0 0 50 40"><path d="M2 38V20C2 10 8 4 18 2l2 6c-6 2-8 5-8 10h8v20zM28 38V20c0-10 6-16 16-18l2 6c-6 2-8 5-8 10h8v20z" fill="var(--orange)"/></svg>
  <p class="abs quote">“Cian’s way of looking at every part of athletic movement and performance has helped me greatly through several of the injuries I have had.<br>The way he breaks my movement down to find the weak links, then plans and coaches to fix those gaps, is invaluable to me and is now one of the key parts of my pre-season over recent years.”</p>
  <div class="abs quote-rule"></div>
  <div class="abs avatar" role="img" aria-label="Portrait of the rugby player"></div>
  <p class="abs who">Rory Dalton</p>
  <p class="abs role">Rugby International, Club Player of the Season</p>
  <svg class="abs arrow" style="left:45px" viewBox="0 0 38 38"><circle cx="19" cy="19" r="19" fill="var(--green)"/><path d="M21 13l-6 6 6 6" stroke="#fff" stroke-width="2" fill="none"/></svg>
  <svg class="abs arrow" style="left:1119px" viewBox="0 0 38 38"><circle cx="19" cy="19" r="19" fill="var(--green)"/><path d="M17 13l6 6-6 6" stroke="#fff" stroke-width="2" fill="none"/></svg>
</section>

<!-- meet -->
<h2 class="abs section-title display" style="left:100px;top:2351px"><span class="accent">Meet With</span><br>Pieter Vosloorink</h2>
<p class="abs body-copy" style="left:100px;top:2450px">Cian Moran PhD MSc blends his work as a sports physiotherapist, strength and conditioning coach, researcher and lecturer, supporting individual athletes and elite squads across a wide range of sports and disciplines. He currently leads Elite Performance and Development at Alvera Clinic, Doha, Qatar, and travels widely to work with athletes and professional clubs. He divides his time between Qatar and Ireland with his wife Sinead and their three children Aoife, Conor and Niamh.</p>
<a class="btn" style="left:100px;top:2622px;width:125px;height:34px">Read More</a>
<div class="abs frame-orange" style="left:705px;top:2283px;width:394px;height:405px"></div>
<div class="abs frame-green" style="left:578px;top:2326px;width:393px;height:405px"></div>
<div class="abs photo-speaker" style="left:590px;top:2295px;width:498px;height:426px" role="img" aria-label="The practitioner speaking at a conference podium"></div>

<!-- events -->
<h2 class="abs display" style="left:0;top:2800px;width:1200px;text-align:center;font-size:33px"><span class="accent">Upcoming</span> Events</h2>
<div class="abs event" style="left:100px">
  <p class="event-date">30 April - 3 May 2025</p>
  <p class="event-name">Advanced Lower Limb Rehabilitation Strategies Athletic Hip and Groin</p>
  <p class="event-place">Brugge, Belgium</p>
</div>
<div class="abs event" style="left:360px">
  <p class="event-date">6-7 June 2025</p>
  <p class="event-name">Advanced Lower Limb Rehabilitation Strategies KineLab, Lausanne, Switzerland</p>
</div>
<div class="abs event" style="left:621px">
  <p class="event-date">15 June 2025</p>
  <p class="event-name">ACL Rehabilitation &amp; Return to Play Decision Making KSR Post Conference Workshop, Milan, Italy Athletic...</p>
</div>
<div class="abs event" style="left:881px">
  <p class="event-date">20-23 November 2025</p>
  <p class="event-name">Athletic Hip and Groin Advanced Thigh Muscle Injury Rehabilitation</p>
  <p class="event-place">Dublin, Ireland</p>
</div>
<a class="btn" style="left:538px;top:3057px;width:124px;height:33px">View More</a>

<!-- footer -->
<footer>
  <div class="abs foot-brand">PVK<small>PERFORMANCE</small></div>
  <span class="abs foot-nav" style="left:334px">About PVK</span>
  <span class="abs foot-nav" style="left:469px">Rehabilitation Specialist</span>
  <span class="abs foot-nav" style="left:713px">Events</span>
  <span class="abs foot-nav" style="left:826px">Contact</span>
  <div class="abs social" style="left:961px" aria-label="Social link"></div>
  <div class="abs social" style="left:1010px" aria-label="Social link"></div>
  <div class="abs social" style="left:1060px" aria-label="Social link"></div>
  <div class="abs foot-rule"></div>
  <p class="abs copyright">© COPYRIGHT ALL RIGHT RESERVED&nbsp; PVK PERFORMANCE 2025</p>
</footer>

</body>
</html>
```